WBP Business Cards

I need business cards for "willow bend partners llc" doublesided... logo on the back (also include logo on front)
logo attached to project... i have jpg up.. let me know if you need eps file.
Company Info:
742 East Harlow Avenue, Suite 8D
Chicago, Illinois 60417
facsimile 312-481-2267 (list fax, address, website on all cards.)
www.willowbendpartnersllc.example
Three different people on cards:
Darius K. Whitcomb, CPA MST
Principal
ofc 312-481-3900
mobile 312-574-8816
dariuskwhitcomb@willowbendpartnersllc.example
Peter J. Olundsen, CPA MST
Principal
peterjolundsen@willowbendpartnersllc.example
mobile 708-613-4471
ofc 312-481-3900
Alvin M Crandby
Principal
ofc 312-481-3900
no mobile
alvinmcrandby@willowbendpartnersllc.example
I have multiple projects listed.. see below:
Business cards for willow bend partners llc
letterhead
envelopes
Business cards for KT Holdings LLC
letterhead
envelopes
Target Market(s)
rich people
Industry/Entity Type
Business
Look and feel

```html
<!DOCTYPE html>
<html lang="en">
<head>
<meta charset="utf-8">
<title>WBP Business Cards</title>
<link rel="stylesheet" href="https://fonts.googleapis.com/css2?family=Gelasio:wght@400;500&display=swap">
<style>
  :root {
    --navy: #1f3f78;
    --navy-soft: #9aa5c6;
    --paper: #f4f5f7;
    --ground: #e3e5ea;
    --ink: #1f3f78;
  }
  * { margin: 0; padding: 0; box-sizing: border-box; }
  html, body { width: 1200px; height: 1000px; overflow: hidden; }
  body {
    background: var(--ground);
    font-family: "Gelasio", Georgia, serif;
    color: var(--ink);
    position: relative;
  }
  .card {
    position: absolute;
    width: 540px;
    height: 310px;
    background: var(--paper);
    border-radius: 14px;
    box-shadow: 0 4px 14px rgba(20, 30, 60, 0.18);
    overflow: hidden;
  }
  .card--back         { left: 40px;  top: 150px; }
  .card--principal-a  { left: 620px; top: 150px; }
  .card--principal-b  { left: 40px;  top: 540px; }
  .card--principal-c  { left: 620px; top: 540px; }

  /* back side */
  .back-mark {
    position: absolute; inset: 0;
    display: flex; align-items: center; justify-content: center; gap: 14px;
  }
  .back-mark .dot { width: 26px; height: 26px; border-radius: 50%; background: var(--navy); }
  .back-mark .wordmark { font-size: 27px; letter-spacing: 0.5px; }

  /* front side */
  .band-top {
    position: absolute; left: 150px; right: 0; top: 48px; height: 6px;
    background: linear-gradient(90deg, rgba(31,63,120,0) 0%, var(--navy-soft) 30%, var(--navy) 100%);
  }
  .band-bottom {
    position: absolute; left: 0; right: 0; top: 252px; height: 6px;
    background: linear-gradient(90deg, var(--navy) 0%, var(--navy) 45%, var(--navy-soft) 80%, rgba(31,63,120,0.1) 100%);
  }
  .front-mark {
    position: absolute; left: 22px; top: 20px;
    display: flex; align-items: center; gap: 6px;
  }
  .front-mark .dot { width: 12px; height: 12px; border-radius: 50%; background: var(--navy); }
  .front-mark .wordmark { font-size: 11px; }
  .fax {
    position: absolute; right: 20px; top: 20px;
    font-size: 14px; display: flex; align-items: center; gap: 6px;
  }
  .website {
    position: absolute; right: 20px; top: 272px; font-size: 14px;
  }
  .person {
    position: absolute; left: 0; right: 0; top: 72px; text-align: center;
  }
  .person .name { font-size: 23px; line-height: 1.2; }
  .person .name--caps { text-transform: uppercase; letter-spacing: 3px; font-size: 21px; }
  .person .title { font-size: 14px; letter-spacing: 5px; margin-top: 2px; }
  .person .address { font-size: 13.5px; line-height: 1.35; margin-top: 12px; }
  .contact-line {
    font-size: 13.5px; line-height: 1.4;
    display: flex; align-items: center; justify-content: center; gap: 6px;
  }
  .phones {
    display: flex; justify-content: space-between; padding: 0 60px; margin-top: 2px;
  }
  .icon { width: 14px; height: 14px; flex: none; }
</style>
</head>
<body>

  <!-- Back: company mark -->
  <section class="card card--back">
    <div class="back-mark">
      <span class="dot"></span>
      <span class="wordmark">Willow Bend Partners llc</span>
    </div>
  </section>

  <!-- Principal card: Whitcomb -->
  <section class="card card--principal-a">
    <div class="band-top"></div>
    <div class="front-mark"><span class="dot"></span><span class="wordmark">Willow Bend Partners llc</span></div>
    <div class="fax">
      <svg class="icon" viewBox="0 0 16 16"><rect x="1" y="6" width="14" height="8" rx="1.5" fill="var(--navy)"/><rect x="4" y="2" width="8" height="5" fill="none" stroke="var(--navy)" stroke-width="1.4"/></svg>
      312-481-2267
    </div>
    <div class="person">
      <div class="name">Darius K. Whitcomb, CPA MST</div>
      <div class="title">Principal</div>
      <div class="address">742 East Harlow Avenue,<br>Suite 8D Chicago, Illinois 60417</div>
      <div class="contact-line">
        <svg class="icon" viewBox="0 0 16 16"><rect x="1" y="3" width="14" height="10" fill="none" stroke="var(--navy)" stroke-width="1.2"/><path d="M1 3l7 6 7-6" fill="none" stroke="var(--navy)" stroke-width="1.2"/></svg>
        dariuskwhitcomb@willowbendpartnersllc.example
      </div>
      <div class="phones">
        <span class="contact-line"><svg class="icon" viewBox="0 0 16 16"><path d="M4 1.5l2.5 3-1.6 1.6a8 8 0 0 0 5 5l1.6-1.6 3 2.5-1.5 2.5C7 14 2 9 1.5 3z" fill="var(--navy)"/></svg>312-481-3900</span>
        <span class="contact-line"><svg class="icon" viewBox="0 0 16 16"><rect x="4" y="1" width="8" height="14" rx="1.5" fill="none" stroke="var(--navy)" stroke-width="1.3"/><circle cx="8" cy="12.5" r="0.9" fill="var(--navy)"/></svg>312-574-8816</span>
      </div>
    </div>
    <div class="band-bottom"></div>
    <div class="website">www.willowbendpartnersllc.example</div>
  </section>

  <!-- Principal card: Crandby -->
  <section class="card card--principal-b">
    <div class="band-top"></div>
    <div class="front-mark"><span class="dot"></span><span class="wordmark">Willow Bend Partners llc</span></div>
    <div class="fax">
      <svg class="icon" viewBox="0 0 16 16"><rect x="1" y="6" width="14" height="8" rx="1.5" fill="var(--navy)"/><rect x="4" y="2" width="8" height="5" fill="none" stroke="var(--navy)" stroke-width="1.4"/></svg>
      312-481-2267
    </div>
    <div class="person">
      <div class="name name--caps">Alvin M Crandby</div>
      <div class="title">Principal</div>
      <div class="address">742 East Harlow Avenue,<br>Suite 8D Chicago, Illinois 60417</div>
      <div class="contact-line">
        <svg class="icon" viewBox="0 0 16 16"><rect x="1" y="3" width="14" height="10" fill="none" stroke="var(--navy)" stroke-width="1.2"/><path d="M1 3l7 6 7-6" fill="none" stroke="var(--navy)" stroke-width="1.2"/></svg>
        alvinmcrandby@willowbendpartnersllc.example
      </div>
      <div class="contact-line">
        <svg class="icon" viewBox="0 0 16 16"><path d="M4 1.5l2.5 3-1.6 1.6a8 8 0 0 0 5 5l1.6-1.6 3 2.5-1.5 2.5C7 14 2 9 1.5 3z" fill="var(--navy)"/></svg>
        312-481-3900
      </div>
    </div>
    <div class="band-bottom"></div>
    <div class="website">www.willowbendpartnersllc.example</div>
  </section>

  <!-- Principal card: Olundsen -->
  <section class="card card--principal-c">
    <div class="band-top"></div>
    <div class="front-mark"><span class="dot"></span><span class="wordmark">Willow Bend Partners llc</span></div>
    <div class="fax">
      <svg class="icon" viewBox="0 0 16 16"><rect x="1" y="6" width="14" height="8" rx="1.5" fill="var(--navy)"/><rect x="4" y="2" width="8" height="5" fill="none" stroke="var(--navy)" stroke-width="1.4"/></svg>
      312-481-2267
    </div>
    <div class="person">
      <div class="name">Peter J. Olundsen, CPA MST</div>
      <div class="title">Principal</div>
      <div class="address">742 East Harlow Avenue,<br>Suite 8D Chicago, Illinois 60417</div>
      <div class="contact-line">
        <svg class="icon" viewBox="0 0 16 16"><rect x="1" y="3" width="14" height="10" fill="none" stroke="var(--navy)" stroke-width="1.2"/><path d="M1 3l7 6 7-6" fill="none" stroke="var(--navy)" stroke-width="1.2"/></svg>
        peterjolundsen@willowbendpartnersllc.example
      </div>
      <div class="phones">
        <span class="contact-line"><svg class="icon" viewBox="0 0 16 16"><path d="M4 1.5l2.5 3-1.6 1.6a8 8 0 0 0 5 5l1.6-1.6 3 2.5-1.5 2.5C7 14 2 9 1.5 3z" fill="var(--navy)"/></svg>312-481-3900</span>
        <span class="contact-line"><svg class="icon" viewBox="0 0 16 16"><rect x="4" y="1" width="8" height="14" rx="1.5" fill="none" stroke="var(--navy)" stroke-width="1.3"/><circle cx="8" cy="12.5" r="0.9" fill="var(--navy)"/></svg>708-613-4471</span>
      </div>
    </div>
    <div class="band-bottom"></div>
    <div class="website">www.willowbendpartnersllc.example</div>
  </section>

</body>
</html>
```